Template for arabic letters worksheet PDF

The contest is to design a pdf worksheet for one Arabic letter. This will be used as a template for the rest of the Arabic alphabet. I am more interested in design and layout as the content can be changed. You don’t have to know Arabic to work on this project as all content will be provided. The winning design may have the opportunity to work on the rest of the project/alphabet work sheets.

Things to keep in mind:
• The worksheets are targeted at children so it should be fun and interesting.
• They will be printable worksheets so do not include colours, it should be a stencil concept.
• I am more interested in design and layout as this will be template for rest of alphabet.
• There is the potential to work on a bigger project.
• DO NOT copy other worksheets I am after creativity.
I HAVE INCLUDED AN EXAMPLE OF A WORKSHEET DO NOT COPY USE IT AS A GUIDE PLEASE.
The following must be included:
• The logo Script kite. Attached
• The letter Alif, ا. It is very similar to a no 1.
• Have the letter ا in a 3d version so children can colour it in.
Include a box for text under or next to the alif. (the text will be provided and the winning entry will add it once all letters are finilized) refer to attatchment
• Have a sketch of a rabbit as it starts with the corresponding letter. (make sure to us an image of a rabbit that can be coloured in) and the word ارنب
• Have one line of the dotted Alif for the children to trace. (refer to example work sheet)
• Have one line blank for the children to practice writing it on their own (refer to example work sheet)
• Have the following in small writing on the bottom left corner. © copyright. Script kite. 2014. All rights reserved.

```html
<!DOCTYPE html>
<html lang="en">
<head>
<meta charset="utf-8">
<title>Letter Alef Worksheet</title>
<link rel="stylesheet" href="https://fonts.googleapis.com/css2?family=Arimo:ital,wght@0,700;1,700&family=Noto+Naskh+Arabic:wght@700&display=swap">
<style>
  :root {
    --ink: #000000;
    --paper: #ffffff;
    --dot: #b5b5b5;
    --fill-soft: #ececec;
  }
  html, body {
    margin: 0;
    padding: 0;
    width: 821px;
    height: 1200px;
    overflow: hidden;
    background: var(--paper);
  }
  .worksheet {
    position: relative;
    width: 821px;
    height: 1200px;
    background: var(--paper);
    font-family: "Arimo", Arial, sans-serif;
  }
  .worksheet-art {
    position: absolute;
    inset: 0;
  }
  .brand {
    position: absolute;
    left: 26px;
    top: 34px;
    display: flex;
    align-items: center;
    gap: 8px;
    font-weight: 700;
    font-size: 24px;
    color: var(--ink);
  }
  .brand-mark {
    width: 16px;
    height: 16px;
    background: var(--ink);
  }
  .thought-text {
    position: absolute;
    left: 326px;
    top: 52px;
    width: 240px;
    margin: 0;
    font-weight: 700;
    font-style: italic;
    font-size: 18.5px;
    line-height: 22px;
    color: var(--ink);
  }
  .rabbit-art {
    position: absolute;
    left: 64px;
    top: 114px;
    width: 210px;
    height: 324px;
    background: linear-gradient(180deg, var(--fill-soft), #f7f7f7);
    border-radius: 40% 40% 30% 30%;
  }
  .letter-word {
    position: absolute;
    left: 298px;
    top: 312px;
    margin: 0;
    font-family: "Noto Naskh Arabic", serif;
    font-weight: 700;
    font-size: 30px;
    color: var(--ink);
    direction: rtl;
  }
  .copyright {
    position: absolute;
    left: 26px;
    top: 1150px;
    margin: 0;
    font-weight: 700;
    font-style: italic;
    font-size: 13px;
    color: var(--ink);
  }
</style>
</head>
<body>
<main class="worksheet">
  <svg class="worksheet-art" width="821" height="1200" viewBox="0 0 821 1200" xmlns="http://www.w3.org/2000/svg">
    <!-- page frame -->
    <rect class="frame" x="10" y="10" width="801" height="1180" fill="none" stroke="var(--ink)" stroke-width="20" rx="10"/>

    <!-- section dividers -->
    <g class="dividers" stroke="var(--ink)" stroke-width="3">
      <line x1="0" y1="438" x2="821" y2="438" stroke-width="0"/>
      <line x1="20" y1="693" x2="801" y2="693"/>
      <line x1="20" y1="914" x2="801" y2="914"/>
      <line x1="82" y1="1012" x2="771" y2="1012" stroke-width="2"/>
      <line x1="82" y1="1122" x2="771" y2="1122" stroke-width="2"/>
    </g>

    <!-- notebook tabs, left -->
    <g class="tabs-left" fill="var(--paper)" stroke="var(--ink)" stroke-width="3">
      <rect x="0" y="470" width="42" height="18"/>
      <rect x="0" y="520" width="45" height="22"/>
      <rect x="0" y="590" width="40" height="18"/>
      <rect x="6" y="638" width="56" height="20"/>
      <rect x="6" y="722" width="38" height="18"/>
      <rect x="0" y="782" width="75" height="20"/>
      <rect x="6" y="838" width="82" height="20"/>
      <rect x="0" y="920" width="55" height="18"/>
      <rect x="0" y="965" width="42" height="18"/>
      <rect x="4" y="1032" width="50" height="20"/>
      <rect x="0" y="1098" width="62" height="20"/>
      <rect x="0" y="1136" width="52" height="16"/>
    </g>

    <!-- notebook tabs, right -->
    <g class="tabs-right" fill="var(--paper)" stroke="var(--ink)" stroke-width="3">
      <rect x="790" y="472" width="31" height="16"/>
      <rect x="788" y="538" width="33" height="18"/>
      <rect x="788" y="605" width="33" height="18"/>
      <rect x="788" y="666" width="33" height="16"/>
      <rect x="788" y="735" width="33" height="16"/>
      <rect x="790" y="804" width="31" height="16"/>
      <rect x="788" y="880" width="33" height="18"/>
      <rect x="788" y="938" width="33" height="20"/>
      <rect x="790" y="1018" width="31" height="20"/>
      <rect x="790" y="1080" width="31" height="18"/>
      <rect x="790" y="1150" width="31" height="18"/>
    </g>

    <!-- thought cloud -->
    <g class="thought-cloud" fill="var(--paper)" stroke="var(--ink)" stroke-width="2.5">
      <path d="M310 170 C 278 160, 280 118, 308 110 C 290 80, 318 52, 345 62 C 350 30, 395 20, 415 40 C 435 14, 485 16, 495 40 C 515 22, 560 28, 560 60 C 590 62, 598 100, 578 118 C 600 140, 582 178, 552 176 C 548 205, 505 214, 488 195 C 470 218, 420 216, 410 194 C 390 212, 345 208, 345 186 C 330 192, 312 186, 310 170 Z"/>
      <ellipse cx="337" cy="218" rx="11" ry="7"/>
      <ellipse cx="320" cy="230" rx="9" ry="6"/>
      <ellipse cx="305" cy="240" rx="7" ry="5"/>
    </g>

    <!-- outlined alef to colour -->
    <g class="alef-outline" fill="var(--paper)" stroke="var(--ink)" stroke-width="3" stroke-linejoin="round">
      <path d="M585 160 L622 153 Q613 280 628 420 L603 424 Q590 300 594 200 Q592 175 585 160 Z"/>
      <path d="M716 155 L756 148 Q746 280 762 418 L733 422 Q720 300 724 200 Q722 170 716 155 Z"/>
      <path class="hamza" d="M712 125 Q716 98 742 100 L762 106 L756 116 Q740 110 732 118 Q745 122 765 118 L760 132 Q732 142 712 135 L698 152 L700 138 Q708 130 712 125 Z"/>
    </g>

    <!-- solid example alef -->
    <path class="alef-solid" d="M736 498 L746 497 Q740 580 748 665 L740 666 Q732 580 736 498 Z" fill="var(--ink)" stroke="var(--ink)" stroke-width="3"/>

    <!-- dotted alef tracing row -->
    <g class="trace-row-plain" stroke="var(--dot)" stroke-width="6" stroke-linecap="round" stroke-dasharray="0 14" fill="none">
      <line x1="91" y1="518" x2="99" y2="658"/>
      <line x1="161" y1="514" x2="167" y2="654"/>
      <line x1="233" y1="516" x2="237" y2="656"/>
      <line x1="295" y1="516" x2="299" y2="656"/>
      <line x1="354" y1="518" x2="360" y2="658"/>
      <line x1="426" y1="518" x2="429" y2="658"/>
      <line x1="502" y1="520" x2="505" y2="660"/>
      <line x1="581" y1="516" x2="584" y2="656"/>
      <line x1="676" y1="516" x2="682" y2="656"/>
    </g>

    <!-- dotted alef with hamza tracing row -->
    <g class="trace-row-hamza" stroke="var(--dot)" stroke-width="6" stroke-linecap="round" stroke-dasharray="0 13" fill="none">
      <g transform="translate(146 0)">
        <line x1="0" y1="755" x2="4" y2="905"/>
        <path d="M-36 735 Q-24 712 -2 714 M-36 735 Q-10 742 14 734 M-4 722 L10 718"/>
      </g>
      <g transform="translate(228 0)">
        <line x1="0" y1="755" x2="4" y2="905"/>
        <path d="M-36 735 Q-24 712 -2 714 M-36 735 Q-10 742 14 734 M-4 722 L10 718"/>
      </g>
      <g transform="translate(319 0)">
        <line x1="0" y1="755" x2="4" y2="905"/>
        <path d="M-36 735 Q-24 712 -2 714 M-36 735 Q-10 742 14 734 M-4 722 L10 718"/>
      </g>
      <g transform="translate(420 0)">
        <line x1="0" y1="755" x2="4" y2="905"/>
        <path d="M-36 735 Q-24 712 -2 714 M-36 735 Q-10 742 14 734 M-4 722 L10 718"/>
      </g>
      <g transform="translate(529 0)">
        <line x1="0" y1="755" x2="4" y2="905"/>
        <path d="M-36 735 Q-24 712 -2 714 M-36 735 Q-10 742 14 734 M-4 722 L10 718"/>
      </g>
      <g transform="translate(620 0)">
        <line x1="0" y1="755" x2="4" y2="905"/>
        <path d="M-36 735 Q-24 712 -2 714 M-36 735 Q-10 742 14 734 M-4 722 L10 718"/>
      </g>
      <g transform="translate(720 0)">
        <line x1="0" y1="755" x2="4" y2="905"/>
        <path d="M-36 735 Q-24 712 -2 714 M-36 735 Q-10 742 14 734 M-4 722 L10 718"/>
      </g>
    </g>
  </svg>

  <div class="brand"><span class="brand-mark"></span>Script kite</div>

  <p class="thought-text">I am the letter Alef. I stand tall, straight and strong with Hamza and without.</p>

  <div class="rabbit-art" role="img" aria-label="Outline drawing of a sitting rabbit to colour in"></div>

  <p class="letter-word" lang="ar">أرنب</p>

  <p class="copyright">©Script kite.2014 copyright.All Rights Reserved</p>
</main>
</body>
</html>
```